Lindenfeld Fabric Atelier needs a sticker for a new pop-up store

We need a sticker (about 13x5 cm) to promote our new pop-up store, where we want to sell haute-couture fabrics and vintage pieces. It should be eye-catching, back ground coulor. The name RIBBON-HERITAGE HOUSE should be read as a block on 3 lines, in the right edge of the name should be a circle with "PLW" in it (like the registered circle) The information "POP-UP-STORE" "AB 4.19. " "MOOSWIESENSTRASSE 7, BAHNHOF WALDENRIED, ZURICH" should be on the sticker as well. The design should be that we are in fashion business, are trendy but have high-quality products.

```html
<!DOCTYPE html>
<html lang="de">
<head>
<meta charset="utf-8">
<title>Lindenfeld Fabric Atelier – Pop-up-Store Sticker</title>
<link rel="stylesheet" href="https://fonts.googleapis.com/css2?family=Bodoni+Moda:opsz,wght@6..96,600&family=Oswald:wght@300;400&display=swap">
<style>
  :root {
    --backdrop: #e8e6e7;
    --sticker-pink: #ef3da6;
    --ink: #1d1a1c;
    --paper: #ffffff;
  }
  html, body {
    margin: 0;
    width: 1200px;
    height: 901px;
    overflow: hidden;
    background: var(--backdrop);
  }
  .canvas {
    position: relative;
    width: 1200px;
    height: 901px;
  }
  .sticker {
    position: absolute;
    left: 80px;
    top: 209px;
    width: 1040px;
    height: 483px;
    background: var(--sticker-pink);
    border-radius: 34px;
    overflow: hidden;
  }
  .name-block {
    position: absolute;
    display: flex;
    align-items: center;
    justify-content: center;
    background: var(--ink);
    font-family: "Bodoni Moda", "Didot", serif;
    font-weight: 600;
    line-height: 1;
    color: var(--paper);
    letter-spacing: 0.01em;
  }
  .name-block--top {
    left: 70px; top: 56px; width: 560px; height: 112px;
    font-size: 104px;
  }
  .name-block--middle {
    left: 112px; top: 167px; width: 612px; height: 112px;
    font-size: 96px;
    color: var(--sticker-pink);
  }
  .name-block--bottom {
    left: 70px; top: 278px; width: 560px; height: 150px;
    font-size: 104px;
    align-items: flex-start;
    padding-top: 14px;
    box-sizing: border-box;
  }
  .brand-seal {
    position: absolute;
    left: 656px;
    top: 62px;
    width: 38px;
    height: 38px;
    border: 2px solid var(--ink);
    border-radius: 50%;
    box-sizing: border-box;
    display: flex;
    align-items: center;
    justify-content: center;
    font-family: "Oswald", "Arial Narrow", sans-serif;
    font-weight: 400;
    font-size: 13px;
    color: var(--ink);
  }
  .store-info {
    position: absolute;
    left: 746px;
    top: 102px;
    width: 278px;
    height: 278px;
    border-radius: 50%;
    background: var(--paper);
    display: flex;
    flex-direction: column;
    align-items: center;
    justify-content: center;
    font-family: "Oswald", "Arial Narrow", sans-serif;
    font-weight: 300;
    font-size: 27px;
    line-height: 1.32;
    text-align: center;
    color: var(--ink);
  }
  .store-info__lead { color: var(--sticker-pink); }
  .store-info p { margin: 0; }
</style>
</head>
<body>
<main class="canvas">
  <section class="sticker" aria-label="Pop-up-Store Sticker">
    <h1 class="brand-name" style="margin:0">
      <span class="name-block name-block--top">RIBBON</span>
      <span class="name-block name-block--middle">HERITAGE</span>
      <span class="name-block name-block--bottom">HOUSE</span>
    </h1>
    <span class="brand-seal">PLW</span>
    <div class="store-info">
      <p class="store-info__lead">POP-UP-STORE</p>
      <p class="store-info__lead">AB 19.04.</p>
      <p>MOOSWIESENSTRASSE 7</p>
      <p>BAHNHOF WALDENRIED</p>
      <p>ZÜRICH</p>
    </div>
  </section>
</main>
</body>
</html>
```